Sole Relationship Graphic of Chapter Organization for Book

This design shows relationships between variables associated with footwear and footprints. It will be used as a graphic in a book. The four elements of the graphic are (1) Variables, (2) Book Chapter Numbers (which correspond to the relationship(s) between at least two variables, (3) Relationship Arrows, and (4) Influence Arrows (because the influencers affect the variables differently than relationships between the variables). These names simply relate to the attempts I have made (and attached) at creating a graphic. In the attached diagrams, the circles with numbers are placeholders for the book chapter numbers, which may be changed so it will be good if I can change those after the graphic is completed. Chapter 1 will be the introduction.
The intent of of outsourcing this project is not necessarily sticking to the formats I have attached, but to allow your creativity to produce a useful graphic that can visually make the most sense of the relationships between the variables as chapters to readers of the book.

Target Market(s)

Search and Rescue Trackers

Requirements
Must have
• Information listed in project description, and drafted in attached diagrams
Nice to have
• Can include outlines of barefoot and outsoles. While Chapters 1 (Intro), 2 (Missing Persons' Footwear), 10 (Case Studies) and 11 (Summary) are set, the others aren't. The end game of this book is to use the rest of the variables to arrive at the end game, which is measurements for barefoot track length or outsole track length...so those two variables can be highlighted in some way to emphasize their importance.

```html
<!DOCTYPE html>
<html lang="en">
<head>
<meta charset="utf-8">
<title>Sole Relationship Diagram – Chapter Organization</title>
<link rel="stylesheet" href="https://fonts.googleapis.com/css2?family=Barlow+Semi+Condensed:wght@500;600;700&display=swap">
<style>
  :root {
    --green: #228b73;
    --slate: #4a5553;
    --legend-border: #6d7472;
    --white: #ffffff;
    --paper: #ffffff;
    --shoe-fill: #d6d6d6;
    --foot-fill: #b71f2a;
  }
  html, body {
    margin: 0;
    padding: 0;
    width: 1200px;
    height: 675px;
    overflow: hidden;
    background: var(--paper);
  }
  .diagram {
    display: block;
    width: 1200px;
    height: 675px;
    font-family: "Barlow Semi Condensed", "Arial Narrow", sans-serif;
  }
  .box-frame { fill: var(--white); stroke: var(--green); stroke-width: 3; }
  .box-band { fill: var(--green); }
  .box-label { fill: var(--white); font-weight: 600; font-size: 19px; text-anchor: middle; }
  .variation-node { fill: var(--slate); }
  .variation-label { fill: var(--white); font-weight: 600; font-size: 22px; text-anchor: middle; }
  .shoe-art { fill: var(--shoe-fill); }
  .foot-art { fill: var(--foot-fill); }
  .track-icon { fill: var(--slate); }
  .link-influence { stroke: var(--green); stroke-width: 4; fill: none; }
  .link-relation { stroke: var(--slate); stroke-width: 4; fill: none; }
  .chapter-badge circle { fill: var(--white); stroke: var(--green); stroke-width: 2.5; }
  .chapter-badge text { fill: var(--slate); font-weight: 700; font-size: 17px; text-anchor: middle; dominant-baseline: central; }
  .side-label { fill: var(--slate); font-weight: 600; font-size: 19px; }
  .track-label { fill: var(--slate); font-weight: 600; font-size: 19px; text-anchor: middle; }
  .legend-title { fill: var(--slate); font-weight: 700; font-size: 23px; }
  .legend-frame { fill: none; stroke: var(--legend-border); stroke-width: 2; }
  .legend-text { fill: var(--slate); font-weight: 600; font-size: 18px; dominant-baseline: central; }
</style>
</head>
<body>
<svg class="diagram" viewBox="0 0 1280 720" xmlns="http://www.w3.org/2000/svg">
  <defs>
    <marker id="head-green" viewBox="0 0 10 10" refX="8" refY="5" markerWidth="4" markerHeight="4" orient="auto-start-reverse">
      <path d="M0 0 L10 5 L0 10 Z" fill="#228b73"/>
    </marker>
    <marker id="head-slate" viewBox="0 0 10 10" refX="8" refY="5" markerWidth="4" markerHeight="4" orient="auto-start-reverse">
      <path d="M0 0 L10 5 L0 10 Z" fill="#4a5553"/>
    </marker>
  </defs>

  <!-- Connections -->
  <g class="connections">
    <line class="link-relation" x1="476" y1="169" x2="801" y2="169" marker-start="url(#head-slate)" marker-end="url(#head-slate)"/>
    <line class="link-influence" x1="185" y1="200" x2="294" y2="200" marker-end="url(#head-green)"/>
    <line class="link-influence" x1="566" y1="230" x2="476" y2="230" marker-end="url(#head-green)"/>
    <line class="link-influence" x1="710" y1="230" x2="801" y2="230" marker-end="url(#head-green)"/>
    <line class="link-influence" x1="637" y1="279" x2="637" y2="366" marker-end="url(#head-green)"/>
    <polyline class="link-influence" points="551,389 408,389 408,295" marker-end="url(#head-green)"/>
    <line class="link-influence" x1="637" y1="407" x2="637" y2="457" marker-end="url(#head-green)"/>
    <polyline class="link-influence" points="361,295 361,507 556,507" marker-start="url(#head-green)" marker-end="url(#head-green)"/>
    <line class="link-influence" x1="497" y1="553" x2="556" y2="553" marker-end="url(#head-green)"/>
    <line class="link-relation" x1="714" y1="523" x2="872" y2="523" marker-end="url(#head-slate)"/>
    <line class="link-relation" x1="977" y1="200" x2="1079" y2="200" marker-end="url(#head-slate)"/>
  </g>

  <!-- Variables -->
  <g class="node node-insole">
    <rect class="box-frame" x="299.5" y="124.5" width="170" height="164"/>
    <rect class="shoe-art" x="318" y="145" width="142" height="80" rx="18" role="img" aria-label="Shoe side view with insole outline highlighted"/>
    <rect class="box-band" x="299.5" y="250" width="170" height="38.5"/>
    <text class="box-label" x="384.5" y="276">Insole</text>
  </g>

  <g class="node node-outsole">
    <rect class="box-frame" x="806.5" y="124.5" width="170" height="164"/>
    <rect class="shoe-art" x="822" y="145" width="144" height="82" rx="18" role="img" aria-label="Shoe side view with outsole outline highlighted"/>
    <rect class="box-band" x="806.5" y="250" width="170" height="38.5"/>
    <text class="box-label" x="891.5" y="276">Outsole</text>
  </g>

  <g class="node node-barefoot">
    <rect class="box-frame" x="563.5" y="462.5" width="150" height="124"/>
    <rect class="foot-art" x="590" y="476" width="98" height="60" rx="10" role="img" aria-label="Bare foot side view"/>
    <rect class="box-band" x="563.5" y="548" width="150" height="38.5"/>
    <text class="box-label" x="638.5" y="574">Barefoot</text>
  </g>

  <g class="node node-variation">
    <rect class="variation-node" x="566" y="200" width="144" height="79" rx="12"/>
    <text class="variation-label" x="638" y="235">Individual</text>
    <text class="variation-label" x="638" y="260">Variation</text>
  </g>

  <g class="node node-nominal-size">
    <rect class="box-band" x="551" y="370" width="173" height="37"/>
    <text class="box-label" x="637.5" y="395">Nominal Size</text>
  </g>

  <!-- Outcomes -->
  <g class="outcome outcome-shod">
    <circle class="track-icon" cx="1125" cy="200" r="44" role="img" aria-label="Shod footprint icon"/>
    <text class="track-label" x="1126" y="266">Shod Track</text>
  </g>
  <g class="outcome outcome-barefoot">
    <circle class="track-icon" cx="923" cy="523" r="45" role="img" aria-label="Barefoot footprint icon"/>
    <text class="track-label" x="923" y="591">Barefoot Track</text>
  </g>

  <!-- Side inputs -->
  <text class="side-label" x="132" y="194">Hook</text>
  <text class="side-label" x="132" y="215">Area</text>
  <text class="side-label" x="433" y="560">Height</text>

  <!-- Chapter numbers -->
  <g class="chapter-badge"><circle cx="638" cy="143" r="13"/><text x="638" y="144">8</text></g>
  <g class="chapter-badge"><circle cx="229" cy="178" r="13"/><text x="229" y="179">3</text></g>
  <g class="chapter-badge"><circle cx="523" cy="252" r="13"/><text x="523" y="253">10</text></g>
  <g class="chapter-badge"><circle cx="749" cy="252" r="13"/><text x="749" y="253">10</text></g>
  <g class="chapter-badge"><circle cx="660" cy="316" r="13"/><text x="660" y="317">10</text></g>
  <g class="chapter-badge"><circle cx="466" cy="411" r="13"/><text x="466" y="412">4</text></g>
  <g class="chapter-badge"><circle cx="661" cy="431" r="13"/><text x="661" y="432">4</text></g>
  <g class="chapter-badge"><circle cx="334" cy="454" r="13"/><text x="334" y="455">5</text></g>
  <g class="chapter-badge"><circle cx="522" cy="579" r="13"/><text x="522" y="580">8</text></g>
  <g class="chapter-badge"><circle cx="796" cy="503" r="13"/><text x="796" y="504">7</text></g>
  <g class="chapter-badge"><circle cx="1026" cy="178" r="13"/><text x="1026" y="179">9</text></g>

  <!-- Legend -->
  <g class="legend">
    <text class="legend-title" x="57" y="520">LEGEND</text>
    <rect class="legend-frame" x="55" y="538" width="264" height="105"/>
    <g class="chapter-badge"><circle cx="145" cy="563" r="12"/><text x="145" y="564">1</text></g>
    <text class="legend-text" x="180" y="563">Chapter #</text>
    <line class="link-relation" x1="63" y1="594" x2="157" y2="594" marker-end="url(#head-slate)"/>
    <text class="legend-text" x="180" y="594">Relationship to</text>
    <line class="link-influence" x1="63" y1="622" x2="157" y2="622" marker-end="url(#head-green)"/>
    <text class="legend-text" x="180" y="622">Influence on</text>
  </g>
</svg>
</body>
</html>
```